Photo Storage Service - Web Application

This is web design for a simple photo storage service.
There is a web page and on the left side is a list of folders and on the right side there are photo thumbnails. By pressing a photo thumbnail, they will see the full size (it's just a link to a different page).
This project is limited only to ONE page, which is the page with the folders list and the thumbnails. However it contains some features that I will try to list here:
- Name of the service: Tavo Vault
- Location of account: http://username.tavo.example
- Folder list: Show all folders belonging to the user. Because you have to be able to drag photos to a folder, they have to be visible and cannot be hidden behind a menu item etc.
- Thumbnails with photos (in the future also videos)
- Adjusted view with smaller thumbnails and less space for folder list (so it is possible to view a larger quantity of thumbnails)- Select multiple thumbnails with rectangle- Show that a thumbnail is selected (maybe bold border?)
- Simple mobile view, but no emphasis on the mobile view in this design project.
- Drag one or more selected photos to a folder
- Delete one or more selected photos
- Drag a folder to another folder
- Rename folder
- Delete folder
- Create folder
- Show progress when deleting/moving (because it calls for every photo, so if there are 100 photos, it will delete 1 by 1 and it will take about 10 seconds - you could show progress bar or equivalent)
Background information: This is for a photo storage service NOT intended for sharing photos, but intended to indefinitely store photos and for yourself to browse your own photos.
It is a design requirement that it loads extremely fast. So we need to limit as much as possible extra graphics that cannot be done by CSS and other external libraries.
(I know this is ONLY design and nothing to do with CSS or libraries, but I can assess from the design if it might be heavy to load when implemented)
I have attached a crude screenshot of the current design, just for your understanding. It should not match this design and you are not in any way supposed to FIT your design into this same style or structure.
Target Market(s)
Consumers
Number of Pages Required
1 page
Font styles to use
Look and feel
Each slider illustrates characteristics of the customer's brand and the style your logo design should communicate.

```html
<!DOCTYPE html>
<html lang="en">
<head>
<meta charset="utf-8">
<title>Tavo Vault – Browse Photos</title>
<link href="https://fonts.googleapis.com/css2?family=Open+Sans:wght@400;600&display=swap" rel="stylesheet">
<style>
:root{
  --bg-top:#3b4fa8;
  --bg-bottom:#a98fdc;
  --bar:#2e3445;
  --side:#1f2435;
  --side-line:#161a27;
  --side-text:#b3bacb;
  --accent:#1e9bf0;
  --panel:#eef1f7;
  --line:#dfe3ea;
  --ink:#3a3f4b;
  --muted:#6b7180;
  --folder:#9fb6d6;
  --white:#ffffff;
}
*{box-sizing:border-box;margin:0;padding:0}
html,body{width:1200px;height:1036px;overflow:hidden}
body{
  font-family:"Open Sans",Arial,sans-serif;
  background:linear-gradient(160deg,var(--bg-top) 0%,#6b74c6 45%,var(--bg-bottom) 100%);
  position:relative;color:var(--ink);
}
.app{position:absolute;left:76px;top:78px;width:1012px;height:896px;background:var(--side);overflow:hidden;box-shadow:0 10px 30px rgba(20,20,60,.25)}
.topbar{position:absolute;left:0;top:0;width:100%;height:33px;background:var(--bar)}
.topbar .links{position:absolute;right:130px;top:0;line-height:33px;font-size:9px;color:#7d8597}
.topbar .links span{margin-left:18px}
.user{position:absolute;right:0;top:0;width:117px;height:33px;background:var(--accent);color:var(--white);font-size:9px;display:flex;align-items:center;padding-left:9px}
.user .avatar{width:22px;height:22px;border-radius:50%;background:#d9e6f2;border:2px solid var(--white);margin-right:8px}
.user svg{margin-left:9px}

.sidebar{position:absolute;left:0;top:33px;width:183px;height:830px}
.brand{height:85px;border-bottom:2px solid var(--side-line);display:flex;flex-direction:column;align-items:center;justify-content:center;gap:8px}
.brand .mark{width:14px;height:14px;border-radius:50%;background:var(--accent)}
.brand .name{font-size:12px;color:#d7dce6;font-weight:600}
.upload{position:absolute;left:26px;top:110px;font-size:10px;color:var(--side-text);display:flex;align-items:center;gap:8px}
.folder-list{position:absolute;left:27px;top:145px;list-style:none}
.folder-list li{font-size:10px;color:var(--side-text);height:28.2px;line-height:28.2px}
.sidebar .split{position:absolute;left:0;top:570px;width:183px;height:3px;background:var(--side-line)}

.main{position:absolute;left:183px;top:33px;width:829px;height:830px;background:var(--white)}
.head{position:absolute;left:0;top:0;width:100%;height:134px;background:var(--panel)}
.title{position:absolute;left:16px;top:18px;font-size:15px;font-weight:400;color:var(--ink)}
.title-rule{position:absolute;left:0;top:52px;width:100%;height:1px;background:var(--line)}
.tabs{position:absolute;left:15px;top:64px;font-size:9px}
.tabs span{position:absolute;top:0;white-space:nowrap;padding:3px 0}
.tabs .active{background:#86a6cf;color:var(--white);border-radius:10px;padding:3px 12px}
.search{position:absolute;left:519px;top:62px;width:296px;height:23px;border:1px solid #cdd3de;border-radius:12px;background:var(--white);font-size:8.5px;color:#8a909c;line-height:21px;padding-left:12px}
.search svg{position:absolute;right:10px;top:5px}
.tool-rule{position:absolute;left:0;top:89px;width:100%;height:1px;background:var(--line)}
.tool{position:absolute;top:98px;width:60px;display:flex;flex-direction:column;align-items:center;gap:3px;font-size:9.5px;color:var(--ink)}
.views{position:absolute;right:23px;top:106px;display:flex;gap:16px}

.label{position:absolute;left:29px;font-size:10.5px;font-weight:600;color:var(--muted)}
.folder{position:absolute;width:124px;height:36px;border:1px solid #cfd4dd;border-radius:4px;font-size:9.5px;display:flex;align-items:center;padding-left:15px;gap:10px;color:var(--ink)}
.folder i{width:15px;height:12px;background:var(--folder);border-radius:1px;display:block}
.thumb{position:absolute;width:122px;height:98px}
.cap{position:absolute;font-size:9px;color:var(--ink);white-space:nowrap}
.check{position:absolute;right:6px;top:8px}
.play{position:absolute;left:50%;top:50%;transform:translate(-50%,-50%)}
.scroll{position:absolute;left:820px;top:151px;width:3px;height:258px;background:#e3e7ee;border-radius:2px}

.footer{position:absolute;left:0;top:863px;width:100%;height:33px;background:var(--side-line)}
.footer .help{position:absolute;right:40px;top:0;width:40px;height:33px;background:#1a1e2b;display:flex;align-items:center;justify-content:center}
.footer .gear{position:absolute;right:0;top:0;width:40px;height:33px;background:var(--accent);display:flex;align-items:center;justify-content:center}
</style>
</head>
<body>
<div class="app">
  <header class="topbar">
    <div class="links"><span>Help Center</span><span>·</span><span>Our Support</span></div>
    <div class="user"><span class="avatar" role="img" aria-label="User avatar"></span>Jane Rowe
      <svg width="9" height="9" viewBox="0 0 10 10"><circle cx="5" cy="5" r="5" fill="#fff"/><path d="M3 4l2 2 2-2" stroke="#1e9bf0" stroke-width="1.3" fill="none"/></svg>
    </div>
  </header>

  <aside class="sidebar">
    <div class="brand"><span class="mark"></span><span class="name">Tavo Vault</span></div>
    <div class="upload">
      <svg width="19" height="13" viewBox="0 0 19 13"><path d="M5 12h9a4 4 0 0 0 0-8 5 5 0 0 0-9.5 1A3.5 3.5 0 0 0 5 12z" fill="#b3bacb"/><path d="M9.5 10V6M7.5 8l2-2 2 2" stroke="#1f2435" stroke-width="1.3" fill="none"/></svg>
      Upload Files
    </div>
    <ul class="folder-list">
      <li>Inbox</li><li>80s party</li><li>A day in oslo</li><li>A tour of Sevenborg</li>
      <li>Alicante 2018</li><li>Alicante after christmas</li><li>Bandarban</li><li>Mobile Uploads</li>
      <li>Random</li><li>Recently upload photo</li><li>Sundarban</li><li>tea garden</li>
    </ul>
    <div class="split"></div>
  </aside>

  <main class="main">
    <div class="head">
      <h1 class="title">Browse Available Phots</h1>
      <div class="title-rule"></div>
      <nav class="tabs">
        <span class="active" style="left:0">Photos</span>
        <span style="left:69px">Videos</span>
        <span style="left:124px">Most Recent</span>
        <span style="left:202px">Most Download</span>
      </nav>
      <div class="search">Enter Keywords
        <svg width="11" height="11" viewBox="0 0 11 11"><circle cx="4.5" cy="4.5" r="3.5" stroke="#6b7180" stroke-width="1.4" fill="none"/><path d="M7 7l3 3" stroke="#6b7180" stroke-width="1.6"/></svg>
      </div>
      <div class="tool-rule"></div>
      <div class="tool" style="left:9px"><svg width="16" height="12" viewBox="0 0 16 12"><path d="M4 11h8a3.5 3.5 0 0 0 0-7 4.5 4.5 0 0 0-8.5 1A3 3 0 0 0 4 11z" fill="#3a3f4b"/></svg>upload</div>
      <div class="tool" style="left:75px"><svg width="16" height="12" viewBox="0 0 16 12"><path d="M4 11h8a3.5 3.5 0 0 0 0-7 4.5 4.5 0 0 0-8.5 1A3 3 0 0 0 4 11z" fill="#3a3f4b"/></svg>download</div>
      <div class="tool" style="left:147px"><svg width="14" height="12" viewBox="0 0 14 12"><path d="M2 11l1-3 7-7 2 2-7 7z" fill="#3a3f4b"/></svg>rename</div>
      <div class="tool" style="left:206px"><svg width="14" height="12" viewBox="0 0 14 12"><path d="M1 2h5l1 1.5h6V11H1z" fill="#3a3f4b"/></svg>create</div>
      <div class="tool" style="left:265px"><svg width="14" height="12" viewBox="0 0 14 12"><path d="M1 2h5l1 1.5h6V11H1z" fill="#3a3f4b"/><path d="M8 6l3 3M11 6l-3 3" stroke="#eef1f7" stroke-width="1.2"/></svg>delete</div>
      <div class="views">
        <svg width="15" height="12" viewBox="0 0 15 12"><rect x="0" y="0" width="7" height="5" fill="#3a3f4b"/><rect x="8" y="0" width="7" height="5" fill="#3a3f4b"/><rect x="0" y="7" width="7" height="5" fill="#3a3f4b"/><rect x="8" y="7" width="7" height="5" fill="#3a3f4b"/></svg>
        <svg width="16" height="12" viewBox="0 0 16 12"><g fill="#3a3f4b"><rect width="3" height="2"/><rect x="4" width="12" height="2"/><rect y="3.3" width="3" height="2"/><rect x="4" y="3.3" width="12" height="2"/><rect y="6.6" width="3" height="2"/><rect x="4" y="6.6" width="12" height="2"/><rect y="10" width="3" height="2"/><rect x="4" y="10" width="12" height="2"/></g></svg>
      </div>
    </div>

    <div class="scroll"></div>

    <h2 class="label" style="top:163px">Folders</h2>
    <div class="folder" style="left:24px;top:185px"><i></i>80’s Party</div>
    <div class="folder" style="left:178px;top:185px"><i></i>A day in oslo</div>
    <div class="folder" style="left:335px;top:185px"><i></i>80’s Party</div>
    <div class="folder" style="left:496px;top:185px"><i></i>A day in oslo</div>
    <div class="folder" style="left:663px;top:185px"><i></i>80’s Party</div>
    <div class="folder" style="left:24px;top:238px"><i></i>80’s Party</div>
    <div class="folder" style="left:178px;top:238px"><i></i>A day in oslo</div>
    <div class="folder" style="left:335px;top:238px"><i></i>80’s Party</div>
    <div class="folder" style="left:496px;top:238px"><i></i>A day in oslo</div>
    <div class="folder" style="left:663px;top:238px"><i></i>80’s Party</div>

    <h2 class="label" style="top:313px">Photo’s</h2>
    <div class="thumb" style="left:26px;top:339px;background:linear-gradient(135deg,#4a2a12,#d8621a 55%,#3a1d0c)" role="img" aria-label="Clownfish among sea anemone"></div>
    <div class="thumb" style="left:155px;top:339px;background:linear-gradient(135deg,#2a2621,#4a4036)" role="img" aria-label="Dimmed portrait photo, selected">
      <svg class="check" width="22" height="22" viewBox="0 0 22 22"><circle cx="11" cy="11" r="10" stroke="#1e9bf0" stroke-width="1.4" fill="none"/><path d="M6.5 11.5l3 3 6-6.5" stroke="#1e9bf0" stroke-width="1.5" fill="none"/></svg>
    </div>
    <div class="thumb" style="left:284px;top:339px;background:linear-gradient(180deg,#b8ad96,#6a5a3c 60%,#8a7350)" role="img" aria-label="Two friends sitting on a wall"></div>
    <div class="thumb" style="left:414px;top:339px;background:linear-gradient(180deg,#e7b05a,#8a6a30 40%,#4e7a2a)" role="img" aria-label="Path through grass at sunset"></div>
    <div class="thumb" style="left:548px;top:339px;background:linear-gradient(135deg,#e0c4a8,#c9a07e 50%,#b23a4a)" role="img" aria-label="Gymnast with a ball"></div>
    <div class="thumb" style="left:681px;top:339px;background:linear-gradient(135deg,#eef0f0,#cfd3d3 60%,#8a6a55)" role="img" aria-label="Woman with hair in the wind"></div>
    <p class="cap" style="left:26px;top:442px">Sad Clown.png</p>
    <p class="cap" style="left:155px;top:442px">Waiting for the train.png</p>
    <p class="cap" style="left:284px;top:442px">Little friends.jpg</p>
    <p class="cap" style="left:414px;top:442px">What A Wonderful.jpg</p>
    <p class="cap" style="left:548px;top:442px">Gymnast.jpg</p>
    <p class="cap" style="left:681px;top:442px">Gymnast.jpg</p>

    <div class="thumb" style="left:26px;top:473px;background:linear-gradient(180deg,#e6d6bd,#c9ae8a)" role="img" aria-label="Legs on a sandy beach"></div>
    <div class="thumb" style="left:155px;top:473px;background:linear-gradient(135deg,#b59677,#7a5a3e)" role="img" aria-label="Sepia portrait photo"></div>
    <div class="thumb" style="left:284px;top:473px;background:linear-gradient(180deg,#b8ad96,#6a5a3c 60%,#8a7350)" role="img" aria-label="Two friends sitting on a wall"></div>
    <div class="thumb" style="left:414px;top:473px;background:linear-gradient(180deg,#9fb2c2,#6c6a62 50%,#5a5448)" role="img" aria-label="Desert landscape with hills"></div>
    <div class="thumb" style="left:548px;top:473px;background:linear-gradient(135deg,#f2ece2,#c9a57a 60%,#9a6a3a)" role="img" aria-label="Shelves with storage baskets"></div>
    <div class="thumb" style="left:681px;top:473px;background:linear-gradient(135deg,#2e3a2a,#44583c 60%,#8a3a3a)" role="img" aria-label="Friends posing among trees"></div>
    <p class="cap" style="left:26px;top:577px">Sad Clown.png</p>
    <p class="cap" style="left:155px;top:577px">Waiting for the train.png</p>
    <p class="cap" style="left:284px;top:577px">Little friends.jpg</p>
    <p class="cap" style="left:414px;top:577px">What A Wonderful.jpg</p>
    <p class="cap" style="left:548px;top:577px">Gymnast.jpg</p>
    <p class="cap" style="left:681px;top:577px">Gymnast.jpg</p>

    <h2 class="label" style="top:622px">Videos</h2>
    <div class="thumb" style="left:26px;top:648px;background:linear-gradient(180deg,#2a6f86,#3f93a6 60%,#1e5466)" role="img" aria-label="Video: woman in the sea">
      <svg class="play" width="26" height="26" viewBox="0 0 26 26"><circle cx="13" cy="13" r="11.5" stroke="#e6e6e6" stroke-width="1.5" fill="rgba(255,255,255,.1)"/><path d="M10.5 8.5l7 4.5-7 4.5z" fill="#e6e6e6"/></svg></div>
    <div class="thumb" style="left:155px;top:648px;background:linear-gradient(135deg,#5e6a3a,#b08a5a 55%,#7a5a3a)" role="img" aria-label="Video: couple outdoors">
      <svg class="play" width="26" height="26" viewBox="0 0 26 26"><circle cx="13" cy="13" r="11.5" stroke="#e6e6e6" stroke-width="1.5" fill="rgba(255,255,255,.1)"/><path d="M10.5 8.5l7 4.5-7 4.5z" fill="#e6e6e6"/></svg></div>
    <div class="thumb" style="left:284px;top:648px;background:linear-gradient(135deg,#3a2a24,#8a6a5a 55%,#4a3630)" role="img" aria-label="Video: close-up portrait">
      <svg class="play" width="26" height="26" viewBox="0 0 26 26"><circle cx="13" cy="13" r="11.5" stroke="#e6e6e6" stroke-width="1.5" fill="rgba(255,255,255,.1)"/><path d="M10.5 8.5l7 4.5-7 4.5z" fill="#e6e6e6"/></svg></div>
    <div class="thumb" style="left:414px;top:648px;background:linear-gradient(180deg,#c79a4e,#6a5a2e 40%,#3e5a22)" role="img" aria-label="Video: path at sunset">
      <svg class="play" width="26" height="26" viewBox="0 0 26 26"><circle cx="13" cy="13" r="11.5" stroke="#e6e6e6" stroke-width="1.5" fill="rgba(255,255,255,.1)"/><path d="M10.5 8.5l7 4.5-7 4.5z" fill="#e6e6e6"/></svg></div>
    <p class="cap" style="left:26px;top:752px">Sad Clown.png</p>
    <p class="cap" style="left:155px;top:752px">Waiting for the train.png</p>
    <p class="cap" style="left:284px;top:752px">Little friends.jpg</p>
    <p class="cap" style="left:414px;top:752px">What A Wonderful.jpg</p>
  </main>

  <footer class="footer">
    <div class="help"><svg width="11" height="11" viewBox="0 0 12 12"><circle cx="6" cy="6" r="6" fill="#fff"/><path d="M4.3 4.6a1.8 1.8 0 1 1 2.4 1.6c-.5.2-.7.5-.7 1V8" stroke="#1a1e2b" stroke-width="1.3" fill="none"/><circle cx="6" cy="9.6" r=".8" fill="#1a1e2b"/></svg></div>
    <div class="gear"><svg width="11" height="11" viewBox="0 0 12 12"><circle cx="6" cy="6" r="3.6" stroke="#fff" stroke-width="2.4" stroke-dasharray="1.9 1" fill="none"/><circle cx="6" cy="6" r="2.4" fill="#fff"/><circle cx="6" cy="6" r="1.1" fill="#1e9bf0"/></svg></div>
  </footer>
</div>
</body>
</html>
```